Prepared Meal Delivery Website

Need a new modern design for a prepared meal delivery company that is hosted on Shopify.

Target Market(s)

Young Professionals

Industry/Entity Type

Prepared Meal Delivery Service

Number of Pages Required

5+ page

Requirements
Must have
• Use https://www.velmorafoods.com/ as an example
Nice to have
• Vibrant page with call to action obvious and repeated
Should not have
• Generic look, grays/white/black

```html
<!DOCTYPE html>
<html lang="en">
<head>
<meta charset="utf-8">
<title>Stride Meals — Peak Nutrition. Peak Performance.</title>
<link href="https://fonts.googleapis.com/css2?family=Jost:wght@400;500;600;700&family=Poppins:wght@600;700;800&display=swap" rel="stylesheet">
<style>
:root{
  --yellow:#f6bd3a;
  --ink:#1e2935;
  --dark:#222222;
  --text:#3a3f45;
  --muted:#6d7278;
  --line:#d8d8d8;
  --paper:#ffffff;
  --topbar:#e7e5e5;
  --slate:#5d6661;
}
*{box-sizing:border-box;margin:0;padding:0}
html,body{width:1200px;height:4543px;overflow:hidden}
body{position:relative;font-family:"Jost",sans-serif;color:var(--text);background:var(--paper)}
.abs{position:absolute}
.ph{position:absolute}
.head{font-family:"Poppins",sans-serif;color:var(--ink);font-weight:700}
.btn{position:absolute;display:flex;align-items:center;justify-content:center;gap:8px;border-radius:22px;font-family:"Poppins",sans-serif;font-weight:700;font-size:12px;letter-spacing:.3px}
.btn svg{width:12px;height:12px}
.btn-dark{background:var(--dark);color:#fff}
.btn-yellow{background:var(--yellow);color:#fff}
.btn-outline{border:2px solid var(--dark);color:var(--dark);background:transparent}

.topbar{left:0;top:0;width:1200px;height:36px;background:var(--topbar);font-size:11px;letter-spacing:.5px;text-align:center;line-height:36px;color:#444}
.header{left:0;top:36px;width:1200px;height:82px;background:#fff}
.logo{position:absolute;left:171px;top:15px;width:187px;height:53px;border:2px solid var(--dark);border-radius:3px;display:flex;align-items:center;justify-content:center;font-weight:600;font-size:18px;letter-spacing:4px;color:var(--dark)}
.mainnav{position:absolute;left:380px;top:0;height:82px;display:flex;gap:27px;align-items:center;font-size:13px;color:#222}
.icons{position:absolute;left:910px;top:32px;display:flex;gap:26px}
.shopbar{left:0;top:118px;width:1200px;height:46px;background:var(--dark);display:flex;justify-content:center;align-items:center;gap:28px;color:#fff;font-size:12px;letter-spacing:1.5px}
.shopbar .sep{color:#aaa}

.hero-tile{top:164px;height:427px}
.hero-caption{left:402px;top:490px;width:396px;height:101px;background:rgba(20,20,20,.78);color:#fff;font-family:"Poppins",sans-serif;font-weight:700;font-size:30px;line-height:46px;text-align:center;padding-top:6px;letter-spacing:1px}

.intro-title{left:0;top:650px;width:1200px;text-align:center;font-size:40px;line-height:46px;font-weight:800;letter-spacing:1px}
.intro-text{left:0;top:766px;width:1200px;text-align:center;font-size:13px}

.badges{left:200px;top:912px;width:800px;display:flex;justify-content:space-between}
.badge{width:80px;height:80px;display:flex;align-items:center;justify-content:center}

.who-title{left:0;top:1066px;width:1200px;text-align:center;font-size:42px;font-weight:800;letter-spacing:1px}
.who{top:1156px;width:290px;text-align:center}
.who .circle{width:247px;height:247px;border-radius:50%;margin:0 auto}
.who h3{font-family:"Poppins",sans-serif;font-weight:700;font-size:17px;color:var(--ink);margin-top:20px;letter-spacing:.5px}
.who p{font-size:12.5px;line-height:20px;margin-top:6px;padding:0 10px}

.test-title{left:0;top:1672px;width:1200px;text-align:center;font-size:36px}
.quote{left:512px;top:1826px;width:462px;text-align:center;font-style:italic;font-size:12.5px;line-height:21px}
.stars{left:512px;width:462px;top:1958px;text-align:center;color:var(--yellow);font-size:18px;letter-spacing:2px}
.person{left:512px;width:462px;top:1986px;text-align:center;font-family:"Poppins",sans-serif;font-weight:700;font-size:18px;color:#333}

.bag{left:0;top:2109px;width:1200px;height:485px;background:var(--yellow)}
.bag-title{left:175px;top:2200px;width:190px;font-size:36px;line-height:46px}
.bag-item{top:2175px;width:210px;text-align:center}
.bag-item .img{width:210px;height:227px}
.bag-item h4{font-family:"Poppins",sans-serif;font-weight:700;font-size:13px;color:var(--ink);margin-top:17px;line-height:22px}
.bag-item p{font-size:12.5px;line-height:22px;color:#4a4036}

.athletes{left:0;top:2594px;width:1200px;height:527px}
.ath-title{left:189px;top:2744px;font-size:38px;color:#fff}
.ath-text{left:192px;top:2812px;width:350px;font-weight:700;font-size:15.5px;line-height:25px;color:#fff}
.ath-card{top:3055px;width:145px}
.ath-card .img{width:145px;height:145px}
.ath-card span{display:block;text-align:center;margin-top:12px;font-family:"Poppins",sans-serif;font-weight:700;font-size:14px;color:var(--ink)}

.mind-title{left:173px;top:3380px;font-size:40px}
.mind-text{left:173px;top:3440px;width:420px;font-size:12.5px;line-height:21px}

.touch{left:0;top:3735px;width:1200px;height:422px;background:linear-gradient(90deg,#e7e5e3,#f1efee 50%,#e6e4e2)}
.touch-title{left:0;top:3860px;width:1200px;text-align:center;font-size:38px}
.email{left:400px;top:3925px;width:431px;height:48px;border-radius:24px;background:#fff;font-size:13px;padding-left:18px;line-height:48px;color:#555}

.fcol{top:4240px}
.fcol h5{font-family:"Poppins",sans-serif;font-weight:700;font-size:15px;color:var(--ink);margin-bottom:24px;letter-spacing:.3px}
.fcol li{list-style:none;font-size:12.5px;color:#666;height:36px}
.contact li{display:flex;gap:12px;align-items:flex-start}

.bottombar{left:0;top:4515px;width:1200px;height:28px;background:var(--dark);color:#fff;font-size:11.5px;line-height:28px;padding-left:173px}
.cards{position:absolute;left:877px;top:5px;display:flex;gap:10px}
.cards i{display:block;width:32px;height:18px;border-radius:2px;background:#d9d9d9}
</style>
</head>
<body>

<div class="abs topbar">ORDERS PLACED NOW WILL BE DELIVERED ON SUNDAY AUG 7TH AND WEDNESDAY AUG 10TH.</div>

<header class="abs header">
  <div class="logo">STRIDE MEALS</div>
  <nav class="mainnav"><span>Meal Plans</span><span>How It Works</span><span>Resources</span><span>Testimonials</span><span>App</span><span>FAQ</span></nav>
  <div class="icons">
    <svg width="16" height="16" viewBox="0 0 16 16"><circle cx="6.5" cy="6.5" r="4.5" fill="none" stroke="#222" stroke-width="2"/><path d="M10 10l4 4" stroke="#222" stroke-width="2"/></svg>
    <svg width="16" height="16" viewBox="0 0 16 16"><circle cx="8" cy="5" r="3.5" fill="#222"/><path d="M1 16c0-4 3-6 7-6s7 2 7 6z" fill="#222"/></svg>
    <svg width="22" height="18" viewBox="0 0 22 18"><path d="M0 2h3l2 9h10l2-7H5" fill="none" stroke="#222" stroke-width="2"/><circle cx="7" cy="15" r="1.6" fill="#222"/><circle cx="14" cy="15" r="1.6" fill="#222"/><circle cx="18" cy="4" r="4" fill="#222"/><text x="18" y="6.5" font-size="6" fill="#fff" text-anchor="middle" font-family="Jost">0</text></svg>
  </div>
</header>

<nav class="abs shopbar"><span>SHOP NOW</span><span class="sep">⋮</span><span>SUBSCRIPTIONS</span><span class="sep">⋮</span><span>BUSINESS PLAN</span><span class="sep">⋮</span><span>GIFT CARDS</span></nav>

<div class="ph hero-tile" style="left:0;width:399px;background:linear-gradient(135deg,#e9e2d6,#c9a45a 55%,#5a3a22)" role="img" aria-label="Meal container with eggs, sausage and greens on a wooden table"></div>
<div class="ph hero-tile" style="left:402px;width:396px;background:linear-gradient(180deg,#6e6a66,#8f8578 60%,#4c4a48)" role="img" aria-label="Woman holding a branded meal bag"></div>
<div class="abs hero-caption">EMPOWERING<br>FOODIES</div>
<div class="ph hero-tile" style="left:801px;width:399px;background:linear-gradient(160deg,#b9b4ad,#d8d4cf 45%,#c8643a 80%,#8a3e23)" role="img" aria-label="Man eating a prepared meal on a sofa"></div>

<h1 class="abs head intro-title">PEAK NUTRITION.<br>PEAK PERFORMANCE.</h1>
<p class="abs intro-text">Lorem ipsum dolor sit amet, consectetur adipiscing elit. Integer aliquet sodales nunc.</p>
<div class="btn btn-yellow" style="left:416px;top:814px;width:179px;height:42px">Shop Meal Plans <svg viewBox="0 0 12 12"><path d="M1 6h9M6 2l4 4-4 4" fill="none" stroke="currentColor" stroke-width="1.6"/></svg></div>
<div class="btn btn-outline" style="left:604px;top:814px;width:180px;height:42px">Take The Quiz <svg viewBox="0 0 12 12"><path d="M1 6h9M6 2l4 4-4 4" fill="none" stroke="currentColor" stroke-width="1.6"/></svg></div>

<div class="abs badges">
  <div class="badge"><svg width="70" height="70"><circle cx="35" cy="35" r="30" fill="#d6d6d6"/></svg></div>
  <div class="badge"><svg width="70" height="70"><rect x="2" y="14" width="66" height="44" fill="#d6d6d6"/></svg></div>
  <div class="badge"><svg width="70" height="70"><circle cx="35" cy="35" r="30" fill="#d6d6d6"/></svg></div>
  <div class="badge"><svg width="70" height="70"><rect x="8" y="8" width="54" height="54" fill="#d6d6d6"/></svg></div>
  <div class="badge"><svg width="70" height="70"><circle cx="35" cy="35" r="30" fill="#d6d6d6"/></svg></div>
  <div class="badge"><svg width="70" height="70"><rect x="8" y="8" width="54" height="54" fill="#d6d6d6"/></svg></div>
</div>

<h2 class="abs head who-title">WHO IS STRIDE FOR</h2>
<div class="abs who" style="left:160px"><div class="circle" style="background:linear-gradient(135deg,#d9d2c8,#a9876a 60%,#6b5240)" role="img" aria-label="Couple holding prepared meals"></div><h3>PROFESSIONAL</h3><p>Stride is the ideal service for the professional on the go. We deliver twice weekly so you can focus on your career and prioritize your business without compromising on nutrition.</p></div>
<div class="abs who" style="left:455px"><div class="circle" style="background:linear-gradient(135deg,#9fb7d1,#e8e3dc 55%,#7f9a5a)" role="img" aria-label="Mother holding her baby outdoors"></div><h3>FAMILIES</h3><p>Set your family up for success with a week of healthy meals planned ahead. By ordering the week before, you'll be able to serve your family healthy meals with minimal effort!</p></div>
<div class="abs who" style="left:748px"><div class="circle" style="background:linear-gradient(135deg,#cfcac4,#6d6a66 55%,#2b2b2b)" role="img" aria-label="Woman eating a meal in a home gym"></div><h3>SINGLES</h3><p>Cooking can be tiring and costly for individuals. Enjoy a clean fridge full of as many or as few meals as you need! No more wasted ingredients, just pure sustainable joy of eating!</p></div>

<h2 class="abs head test-title">What People Say About Us</h2>
<div class="ph" style="left:210px;top:1756px;width:268px;height:274px;background:linear-gradient(160deg,#8a7f6e,#c8bfb2 50%,#5f7e86)" role="img" aria-label="Customer crouching beside a meal delivery bag"></div>
<p class="abs quote">"Great service, tasty food, affordable prices. We were doing those complicated meal prep kits for so long until we found Stride. Basically the same healthy, delicious meals for the same price... But they're already prepared and cooked!! All you do is reheat! Kid-friendly and vegan options? With outstanding customer service? Could not get better. So glad we found Stride."</p>
<div class="abs stars">★★★★★</div>
<div class="abs person">Maribel</div>
<svg class="abs" style="left:170px;top:1888px" width="30" height="56"><path d="M26 2L4 28l22 26" fill="none" stroke="#333" stroke-width="2"/></svg>
<svg class="abs" style="left:998px;top:1888px" width="30" height="56"><path d="M4 2l22 26L4 54" fill="none" stroke="#333" stroke-width="2"/></svg>

<section class="abs bag"></section>
<h2 class="abs head bag-title">What's in<br>Your<br>Stride<br>Bag ?</h2>
<div class="btn btn-dark" style="left:173px;top:2413px;width:180px;height:38px">CHOOSE YOUR PLAN <svg viewBox="0 0 12 12"><path d="M1 6h9M6 2l4 4-4 4" fill="none" stroke="currentColor" stroke-width="1.6"/></svg></div>
<div class="abs bag-item" style="left:372px"><div class="img" style="background:linear-gradient(135deg,#e6e2dc,#b8503e 50%,#6f8c4a)" role="img" aria-label="Rows of prepared salad meals"></div><h4>Delicious Chef-inspired Meals</h4><p>Our meals are designed and<br>prepared by a team</p></div>
<div class="abs bag-item" style="left:597px"><div class="img" style="background:linear-gradient(160deg,#d6cfc5,#8c6a52 55%,#5b4638)" role="img" aria-label="Athlete holding a portioned meal"></div><h4>Perfectly portioned Amounts</h4><p>Each product is comprised of<br>portioned ingredients</p></div>
<div class="abs bag-item" style="left:819px"><div class="img" style="background:linear-gradient(160deg,#e4dfd8,#c9a27a 55%,#b74a36)" role="img" aria-label="Woman showing a meal and recyclable packaging"></div><h4>Recyclable ice packs and Packaging</h4><p>Our meals and other products</p></div>
<div class="btn btn-outline" style="left:409px;top:2501px;width:136px;height:37px">READ MROE <svg viewBox="0 0 12 12"><path d="M1 6h9M6 2l4 4-4 4" fill="none" stroke="currentColor" stroke-width="1.6"/></svg></div>
<div class="btn btn-outline" style="left:632px;top:2501px;width:136px;height:37px">READ MROE <svg viewBox="0 0 12 12"><path d="M1 6h9M6 2l4 4-4 4" fill="none" stroke="currentColor" stroke-width="1.6"/></svg></div>
<div class="btn btn-outline" style="left:856px;top:2501px;width:136px;height:37px">READ MROE <svg viewBox="0 0 12 12"><path d="M1 6h9M6 2l4 4-4 4" fill="none" stroke="currentColor" stroke-width="1.6"/></svg></div>

<section class="ph athletes" style="background:linear-gradient(90deg,#58625d 0%,#5f6863 40%,#9c9a96 62%,#c65e3a 85%,#a8492d 100%)" role="img" aria-label="Man eating a meal on a sofa"></section>
<h2 class="abs head ath-title">We Build Athletes</h2>
<p class="abs ath-text">Integer viverra lectus sed condimentum elementum. Quisque lacus fringilla odio tempus, nec lobortis</p>
<div class="btn btn-dark" style="left:194px;top:2903px;width:182px;height:39px">CHOOSE YOUR PLAN <svg viewBox="0 0 12 12"><path d="M1 6h9M6 2l4 4-4 4" fill="none" stroke="currentColor" stroke-width="1.6"/></svg></div>
<div class="abs ath-card" style="left:196px"><div class="img" style="background:linear-gradient(180deg,#8fb4d8,#c9d2cf 60%,#7c7f78)" role="img" aria-label="Athlete walking with a meal bag"></div><span>Mauris pharetra</span></div>
<div class="abs ath-card" style="left:361px"><div class="img" style="background:linear-gradient(180deg,#4d6f7d,#d5cab4 60%,#5b5a55)" role="img" aria-label="Athlete holding a meal bag at a doorway"></div><span>Mauris pharetra</span></div>
<div class="abs ath-card" style="left:527px"><div class="img" style="background:linear-gradient(180deg,#e4ddd3,#a78670 60%,#5e4a3e)" role="img" aria-label="Athlete holding a meal bag"></div><span>Mauris pharetra</span></div>
<div class="abs ath-card" style="left:692px"><div class="img" style="background:linear-gradient(180deg,#bfc3c4,#6f7f86 55%,#3c4a52)" role="img" aria-label="Athlete seated with a meal"></div><span>Mauris pharetra</span></div>
<div class="abs ath-card" style="left:858px"><div class="img" style="background:linear-gradient(180deg,#cfc9c1,#3f8fb0 50%,#2b2b2b)" role="img" aria-label="Athlete holding meal containers"></div><span>Mauris pharetra</span></div>

<h2 class="abs head mind-title">Mind. Body. Social.</h2>
<p class="abs mind-text">Integer viverra lectus sed condimentum elementum. Quisque rutrum lacus fringilla odio tempus, nec lobortis dui interdum. Aenean ultrices felis in mollis dapibus. Suspendisse potenti. Sed eget commodo erat. Aenean at semper erat. Morbi efficitur, nunc quis pellentesque mollis,</p>
<div class="btn btn-dark" style="left:173px;top:3544px;width:180px;height:39px">CHOOSE YOUR PLAN <svg viewBox="0 0 12 12"><path d="M1 6h9M6 2l4 4-4 4" fill="none" stroke="currentColor" stroke-width="1.6"/></svg></div>
<svg class="abs" style="left:640px;top:3380px" width="380" height="260">
  <path d="M55 180 A 140 140 0 0 1 335 180" fill="none" stroke="#555" stroke-width="1" stroke-dasharray="3 4"/>
  <circle cx="180" cy="45" r="38" fill="#fff"/>
  <circle cx="55" cy="195" r="38" fill="#fff"/>
  <circle cx="313" cy="190" r="38" fill="#fff"/>
</svg>
<div class="ph" style="left:782px;top:3388px;width:76px;height:76px;border-radius:50%;border:2px solid var(--ink)" role="img" aria-label="Line icon of a flexed arm"></div>
<div class="ph" style="left:657px;top:3537px;width:76px;height:76px;border-radius:50%;border:2px solid var(--ink)" role="img" aria-label="Line icon of a head with a brain"></div>
<div class="ph" style="left:915px;top:3532px;width:76px;height:76px;border-radius:50%;border:2px solid var(--ink)" role="img" aria-label="Line icon of social media symbols"></div>

<section class="abs touch"></section>
<div class="ph" style="left:0;top:3735px;width:330px;height:422px;background:radial-gradient(circle at 30% 50%,#e08a3a,#6f8d3d 45%,#3a3f44 70%,transparent 72%)" role="img" aria-label="Plate of chicken, broccoli and sweet potato fries"></div>
<div class="ph" style="left:880px;top:3735px;width:320px;height:422px;background:radial-gradient(circle at 70% 50%,#d2462a,#e87a4a 30%,#f3efe9 55%,transparent 70%)" role="img" aria-label="Plate of stuffed peppers in tomato sauce"></div>
<h2 class="abs head touch-title">Keep In Touch</h2>
<div class="abs email">Enter email address</div>
<div class="btn btn-dark" style="left:510px;top:3984px;width:178px;height:40px">CHOOSE YOUR PLAN <svg viewBox="0 0 12 12"><path d="M1 6h9M6 2l4 4-4 4" fill="none" stroke="currentColor" stroke-width="1.6"/></svg></div>

<footer>
  <div class="abs fcol contact" style="left:173px"><h5>WE'RE HERE TO HELP!</h5><ul>
    <li><svg width="14" height="12" viewBox="0 0 14 12"><rect x="0" y="1" width="14" height="10" fill="#333"/><path d="M0 1l7 6 7-6" fill="none" stroke="#fff" stroke-width="1.2"/></svg>info@stridemeals.com</li>
    <li><svg width="14" height="14" viewBox="0 0 14 14"><path d="M3 0l3 3-2 2c1 2 3 4 5 5l2-2 3 3-2 3C6 13 1 8 0 2z" fill="#333"/></svg>(416) 555 0142</li></ul></div>
  <div class="abs fcol" style="left:425px"><h5>MENU</h5><ul><li>Meal menu</li><li>How it works</li><li>Contact us</li><li>Term of service</li></ul></div>
  <div class="abs fcol" style="left:538px;top:4288px"><ul><li>Refund policy</li><li>Shipping policy</li><li>Privacy policy</li></ul></div>
  <div class="abs fcol" style="left:716px"><h5>OTHER LINKS</h5><ul><li>My Account</li><li>Wishlist</li><li>My cart</li><li>Order Details</li><li>Payment Method</li></ul></div>
  <div class="abs fcol" style="left:909px"><h5>POLICY</h5><ul><li>Term of condition</li><li>Refund</li><li>Shipping Policy</li><li>Privacy Policy</li></ul></div>
  <div class="abs bottombar">© 2022 <b>Stride Meals</b> All right reserved
    <div class="cards"><i></i><i></i><i></i><i></i></div>
  </div>
</footer>

</body>
</html>
```